VELMOTIK Amazing Business Cards Challenge

Velmoti is a new technology company that will provide engineering and manufacturing services in the electric vehicle industry.

We are looking at a new business card that will support our orientation in providing advanced, innovative solutions. The business card will be lean and present the only information required to be more efficient.

Target Market(s)

Fleet operators, private commercial vehicle operators, delivery companies.

Industry/Entity Type

Business

Contact Information for Business Card

Use the logo and its colors, use a white background.

Font styles to use
Sans Serif

Colors
0455a3
ffffff
9bcb3c

Requirements
Must have
• Velmotik Logo
• All informations in the DOC file = 3 different cards.
• White background
Nice to have
• Icons for email, phone and web address.
• Cute design and strong identity.
Should not have
• Bleeds

```html
<!DOCTYPE html>
<html lang="fr">
<head>
<meta charset="utf-8">
<title>Velmotik — Business Card</title>
<link href="https://fonts.googleapis.com/css2?family=Arimo:wght@400;700&display=swap" rel="stylesheet">
<style>
  :root {
    --stage: #2b2b2d;
    --brand-blue: #0b5a8a;
    --brand-blue-deep: #07466d;
    --accent-blue: #1a8fd0;
    --panel-dark: #353538;
    --panel-grey: #8a8a8d;
    --paper: #ffffff;
    --paper-shade: #ececec;
    --ink: #222326;
  }
  * { margin: 0; padding: 0; box-sizing: border-box; }
  html, body {
    width: 1200px; height: 1000px; overflow: hidden;
    background: var(--stage);
    font-family: "Arimo", Arial, sans-serif;
  }
  .stage { position: relative; width: 1200px; height: 1000px; }

  .card {
    position: absolute; width: 700px; height: 400px; overflow: hidden;
    box-shadow: 0 12px 30px rgba(0,0,0,.45);
  }

  /* Front */
  .card-front {
    left: 110px; top: 70px;
    background: linear-gradient(160deg, var(--brand-blue) 0%, var(--brand-blue-deep) 100%);
    display: flex; align-items: center; justify-content: center;
  }
  .brand-lockup { display: flex; align-items: center; gap: 22px; }
  .brand-mark { width: 54px; height: 54px; background: var(--paper); }
  .brand-name {
    color: var(--paper); font-weight: 400; font-size: 84px; letter-spacing: 2px;
    line-height: 1;
  }

  /* Back */
  .card-back { left: 390px; top: 520px; background: var(--paper); }
  .card-back svg.back-shapes { position: absolute; inset: 0; }

  .identity { position: absolute; left: 418px; top: 26px; max-width: 230px; }
  .identity-name { color: var(--accent-blue); font-weight: 700; font-size: 23px; white-space: nowrap; }
  .identity-degree { color: var(--panel-grey); font-size: 17px; margin: 4px 0 0 14px; }
  .identity-title { color: var(--panel-grey); font-size: 11px; margin: 3px 0 0 14px; }

  .contact-list {
    position: absolute; left: 40px; top: 182px; width: 340px; list-style: none;
    color: var(--ink); font-size: 17px; font-weight: 700; letter-spacing: 0;
  }
  .contact-list li { display: flex; align-items: flex-start; gap: 9px; margin-bottom: 9px; line-height: 1.2; white-space: nowrap; }
  .contact-icon { width: 17px; height: 17px; flex: none; margin-top: 2px; }
</style>
</head>
<body>
<main class="stage">

  <section class="card card-front" aria-label="Card front">
    <div class="brand-lockup">
      <span class="brand-mark" aria-hidden="true"></span>
      <span class="brand-name">velmotik</span>
    </div>
  </section>

  <section class="card card-back" aria-label="Card back">
    <svg class="back-shapes" width="700" height="400" viewBox="0 0 700 400" aria-hidden="true">
      <defs>
        <linearGradient id="paperFade" x1="0" y1="0" x2="1" y2="1">
          <stop offset="0" stop-color="#ffffff"/>
          <stop offset="1" stop-color="#e9e9e9"/>
        </linearGradient>
      </defs>
      <rect width="700" height="400" fill="url(#paperFade)"/>
      <rect x="400" y="0" width="300" height="380" fill="var(--panel-dark)"/>
      <rect x="640" y="0" width="30" height="70" fill="var(--paper-shade)"/>
      <polygon points="670,70 700,40 700,300" fill="var(--brand-blue)"/>
      <polygon points="330,330 400,310 400,380 310,380" fill="var(--accent-blue)"/>
      <rect x="0" y="384" width="700" height="16" fill="var(--accent-blue)"/>
      <rect x="30" y="0" width="4" height="165" fill="var(--accent-blue)"/>
      <rect x="39" y="0" width="4" height="165" fill="var(--accent-blue)"/>
    </svg>

    <div class="identity">
      <p class="identity-name">Julien Marchand,</p>
      <p class="identity-degree">ing, M.Sc.A.</p>
      <p class="identity-title">Président | CEO</p>
    </div>

    <ul class="contact-list">
      <li>
        <svg class="contact-icon" viewBox="0 0 18 18" aria-label="Phone"><rect width="18" height="18" rx="2" fill="var(--accent-blue)"/><path d="M5 4h3l1 3-2 1a7 7 0 0 0 3 3l1-2 3 1v3a1 1 0 0 1-1 1A10 10 0 0 1 4 5a1 1 0 0 1 1-1z" fill="#fff"/></svg>
        +1.514.555.0187
      </li>
      <li>
        <svg class="contact-icon" viewBox="0 0 18 18" aria-label="Email"><rect width="18" height="18" rx="2" fill="var(--accent-blue)"/><rect x="3.5" y="5" width="11" height="8" fill="none" stroke="#fff" stroke-width="1.4"/><path d="M3.5 5l5.5 4.5L14.5 5" fill="none" stroke="#fff" stroke-width="1.4"/></svg>
        jmarchand@velmotik.com
      </li>
      <li>
        <svg class="contact-icon" viewBox="0 0 18 18" aria-label="Website"><rect width="18" height="18" rx="2" fill="var(--accent-blue)"/><circle cx="9" cy="9" r="5.5" fill="none" stroke="#fff" stroke-width="1.3"/><ellipse cx="9" cy="9" rx="2.3" ry="5.5" fill="none" stroke="#fff" stroke-width="1.1"/><path d="M3.5 9h11" stroke="#fff" stroke-width="1.1"/></svg>
        velmotik.com
      </li>
      <li>
        <svg class="contact-icon" viewBox="0 0 18 18" aria-label="Address"><rect width="18" height="18" rx="2" fill="var(--accent-blue)"/><path d="M9 3.5l6 5.5h-2v5.5H10.5v-3.5h-3v3.5H5V9H3z" fill="#fff"/></svg>
        <span>410 – 218 Rue Valcourt,<br>Montréal (Québec) H2L 3K6 Canada</span>
      </li>
    </ul>
  </section>

</main>
</body>
</html>
```